■ 依頼内容・記事LPで使用する 正方形バナー(1080×1080) のデザインを募集します。 ・こちらで用意する コピー(テキスト)を必ず使用し、 クリックしたくなる視認性・訴求力の高いデザインに仕上げてください。 用途:記事LP内/広告・SNS投稿等でも流用予定 制作物:1080×1080 正方形バナー(静止画) 方向性:読みやすい・強い訴求・スマホで映える(細かすぎる情報はNG) ■ バナーに入れるコピー ・2026年最新版 ・千葉県の不用品回収 ・おすすめ業者TOP3 ■ 納品形式 ・採用者の最終納品は Canva(編集可能なデザインデータ)でお願いします。 ※デザインデータごと買い取りたいので、他の人が画像や文字を変更して使いやすい状態にしていただけると助かります◎ ・Canvaのリンク共有(編集可)+書き出しデータ(PNG)も希望 ・Canvaは 有料素材の使用OK(ただしライセンス的に問題ない使い方でお願いします) ■ デザイン要件 サイズ:1080×108 0テキスト:こちら指定のコピーを使用 フォント:商用利用可能なもの(Canva標準フォント推奨) 素材:商用利用可能なもののみ(Canva素材 or 権利クリア済のもの) 仕上がり:スマホで見て一瞬で内容が伝わることを最優先 ■ 採用後にお願いしたいこと (軽微な修正)採用後、こちらのフィードバックに沿って配色微調整文字サイズ・余白調整CTA表現の微調整など 1〜2回程度の修正をお願いする可能性があります。 ■ 応募時(提案)で見たいもの コンペ提出物:1080×1080 バナー案(PNGでOK) ■ 選定基準 クリックしたくなる強さ(訴求力) 可読性(スマホで一瞬で読める) 記事LPに馴染む品質(安っぽく見えない) Canva編集前提の設計(差し替えやすさ) ■ 注意事項 ・納品データは Canva編集可能な状態でのご提出をお願いします ・使用素材は 商用利用可能な範囲に限ります ・採用案の著作権/利用権は当方に譲渡(買い取り)希望です ■ 依頼料金1枚 5,500円(税込) ※契約金額(税込)からシステム利用料を差し引いた金額が、 ワーカーさまの受取金額となります◎ ご応募をお待ちしております! |
もっともよかったです。
皆様ありがとうございました。

```html
<!DOCTYPE html>
<html lang="ja">
<head>
<meta charset="UTF-8">
<title>千葉県の不用品回収 おすすめ業者TOP3</title>
<link rel="stylesheet" href="https://fonts.googleapis.com/css2?family=Noto+Sans+JP:wght@700;900&family=Montserrat:wght@800;900&display=swap">
<style>
  :root {
    --navy: #1f4b8e;
    --yellow: #f8ea45;
    --lime: #e4f2a6;
    --panel: rgba(255, 255, 255, 0.86);
    --bg-light: #f3efe8;
    --bg-warm: #d9c3a2;
    --bg-mid: #e8e2d8;
  }
  * { margin: 0; padding: 0; box-sizing: border-box; }
  html, body { width: 1200px; height: 1200px; overflow: hidden; background: #fff; }
  .banner {
    position: relative;
    width: 1200px;
    height: 1200px;
    overflow: hidden;
    font-family: "Noto Sans JP", sans-serif;
    color: var(--navy);
  }
  .hero-photo {
    position: absolute;
    inset: 0;
    background:
      linear-gradient(180deg, rgba(255,255,255,0) 55%, rgba(199,160,110,0.55) 100%),
      radial-gradient(circle at 12% 30%, #cfd6de 0%, rgba(207,214,222,0) 35%),
      linear-gradient(135deg, var(--bg-light) 0%, var(--bg-mid) 55%, var(--bg-warm) 100%);
  }
  .content-panel {
    position: absolute;
    left: 100px;
    top: 100px;
    width: 1000px;
    height: 1008px;
    background: var(--panel);
  }
  .edition-ribbon {
    position: absolute;
    left: 385px;
    top: 150px;
    width: 430px;
    height: 86px;
  }
  .edition-ribbon span {
    position: absolute;
    inset: 0;
    display: flex;
    align-items: center;
    justify-content: center;
    color: #fff;
    font-weight: 900;
    font-size: 52px;
    letter-spacing: 1px;
  }
  .region {
    position: absolute;
    top: 290px;
    left: 0;
    width: 100%;
    text-align: center;
    font-weight: 900;
    font-size: 96px;
    line-height: 1;
    letter-spacing: 4px;
  }
  .region-swash {
    position: absolute;
    left: 340px;
    top: 405px;
    width: 520px;
    height: 40px;
  }
  .service {
    position: absolute;
    top: 468px;
    left: 0;
    width: 100%;
    text-align: center;
    font-weight: 900;
    font-size: 176px;
    line-height: 1.1;
    letter-spacing: 4px;
    color: var(--yellow);
    -webkit-text-stroke: 10px var(--navy);
    paint-order: stroke fill;
    text-shadow: 9px 9px 0 var(--navy);
  }
  .ranking-lead {
    position: absolute;
    left: 232px;
    top: 722px;
    font-weight: 900;
    font-size: 62px;
    line-height: 1;
    letter-spacing: 2px;
  }
  .ranking-top {
    position: absolute;
    left: 272px;
    top: 808px;
    font-family: "Montserrat", sans-serif;
    font-weight: 900;
    font-size: 132px;
    line-height: 1;
    letter-spacing: 8px;
  }
  .ranking-number {
    position: absolute;
    left: 718px;
    top: 690px;
    font-family: "Montserrat", sans-serif;
    font-weight: 900;
    font-size: 290px;
    line-height: 1;
    color: var(--lime);
    -webkit-text-stroke: 8px var(--navy);
    paint-order: stroke fill;
    transform: skewX(-6deg);
  }
  .ranking-rule {
    position: absolute;
    left: 318px;
    top: 948px;
    width: 565px;
    height: 4px;
    background: var(--navy);
  }
  .sparkle { position: absolute; left: 905px; top: 715px; width: 70px; height: 80px; }
  .chevrons { position: absolute; left: 862px; top: 998px; width: 210px; height: 58px; }
</style>
</head>
<body>
  <main class="banner">
    <div class="hero-photo" role="img" aria-label="段ボール箱に荷物を詰める女性の明るい室内写真"></div>
    <div class="content-panel"></div>

    <div class="edition-ribbon">
      <svg width="430" height="86" viewBox="0 0 430 86" aria-hidden="true">
        <polygon points="0,0 430,0 408,43 430,86 0,86 22,43" fill="var(--navy)"/>
      </svg>
      <span>2026年最新版</span>
    </div>

    <h1 class="region">千葉県の</h1>
    <svg class="region-swash" viewBox="0 0 520 40" aria-hidden="true">
      <path d="M0,22 C120,8 200,10 245,20 L260,32 L275,20 C320,10 400,8 520,22" fill="none" stroke="var(--navy)" stroke-width="3"/>
    </svg>

    <p class="service">不用品回収</p>

    <p class="ranking-lead">おすすめ業者</p>
    <p class="ranking-top">TOP</p>
    <p class="ranking-number">3</p>
    <svg class="sparkle" viewBox="0 0 70 80" aria-hidden="true">
      <g stroke="var(--navy)" stroke-width="4" stroke-linecap="round">
        <line x1="10" y1="38" x2="30" y2="12"/>
        <line x1="22" y1="50" x2="58" y2="36"/>
        <line x1="26" y1="64" x2="56" y2="66"/>
      </g>
    </svg>
    <div class="ranking-rule"></div>

    <svg class="chevrons" viewBox="0 0 210 58" aria-hidden="true">
      <g fill="var(--yellow)" stroke="var(--navy)" stroke-width="3" stroke-linejoin="round">
        <polygon points="4,4 26,4 48,29 26,54 4,54 26,29"/>
        <polygon points="52,4 74,4 96,29 74,54 52,54 74,29"/>
        <polygon points="100,4 122,4 144,29 122,54 100,54 122,29"/>
        <polygon points="148,4 170,4 192,29 170,54 148,54 170,29"/>
      </g>
    </svg>
  </main>
</body>
</html>
```